Create a Branded Four Stage Lifecycle Diagram

We need a rethink / redesign of our Lifecycle. We created it and have used it till now but it is not professional and needs our branding as well. We use it for presentations, for analysis with schools when we are consulting on site and it should look equally good on a powerpoint slide as on a handout and, of course, as a JPG that we can copy onto documents that we create. It does not have to look like what we currently have. I will include the article so you can see what we are trying to achieve. Eventually we want to be able to trademark it. It should include copyright 2020 Harbor Academy Advisors. Each stafe should reflect its characteristics in some fashion.

Target Market(s)

We serve K-12 Christian private schools

Industry/Entity Type

Education

Font styles to use
Sans Serif

Colors

Designer to choose colors to be used in the design.

Requirements
Must have
• HAA logo
• copyright notice
• title: HAA Lifecycle
Nice to have
• In the article, you will see the Corporate Lifecycle. It is completely different from ours. You will also see our current 'design'. It does not have to be like the one we currently have - it is not a refresh - it is a new design.
Should not have
• There must be no chance that our design could be confused with the corporate lifecycle.

```html
<!DOCTYPE html>
<html lang="en">
<head>
<meta charset="UTF-8">
<title>The HAA Christian School Lifecycle</title>
<link href="https://fonts.googleapis.com/css2?family=EB+Garamond:wght@400;600&family=Open+Sans:wght@700&family=Poppins:wght@400;500;600&display=swap" rel="stylesheet">
<style>
  :root {
    --bg: #ffffff;
    --title-blue: #1a6f9a;
    --title-deep: #0e4d6e;
    --ink: #222222;
    --sky: #22b8ea;
    --green: #1c8c4b;
    --red: #d9323f;
    --violet: #7a4cc8;
  }
  * { margin: 0; padding: 0; box-sizing: border-box; }
  html, body { width: 1200px; height: 675px; overflow: hidden; background: var(--bg); }
  .canvas { position: relative; width: 1200px; height: 675px; background: var(--bg); }
  .page-title {
    position: absolute; top: 24px; left: 0; width: 100%;
    text-align: center;
    font-family: "EB Garamond", Georgia, serif;
    font-weight: 400; font-size: 27px; color: var(--title-blue);
  }
  .page-title strong { font-weight: 600; color: var(--title-deep); }
  .lifecycle { position: absolute; inset: 0; }
  .stage-name { font-family: "Open Sans", Arial, sans-serif; font-weight: 700; font-size: 17px; fill: #fff; }
  .stage-age { font-family: "Poppins", Arial, sans-serif; font-size: 9.5px; fill: #fff; }
  .brand-name {
    position: absolute; left: 40px; top: 612px;
    font-family: "Poppins", Arial, sans-serif; font-weight: 600;
    font-size: 34px; line-height: 1; color: var(--ink);
  }
  .copyright {
    position: absolute; right: 24px; top: 624px;
    font-family: "Poppins", Arial, sans-serif; font-weight: 500;
    font-size: 12.5px; color: var(--ink);
  }
</style>
</head>
<body>
<div class="canvas">
  <h1 class="page-title">The HAA Christian School “<strong>Lifecycle</strong>”</h1>

  <svg class="lifecycle" width="1200" height="675" viewBox="0 0 1280 720" aria-label="Four stage lifecycle: Entrepreneur, Adolescent, Mature, Dying">
    <g class="connectors" stroke="#c8cdd3" stroke-width="2" fill="none">
      <line x1="385" y1="350" x2="440" y2="362"/>
      <line x1="582" y1="400" x2="640" y2="396"/>
      <line x1="790" y1="340" x2="838" y2="292"/>
    </g>

    <g class="stage stage-entrepreneur">
      <circle cx="321" cy="302" r="84" fill="#fff" stroke="var(--sky)" stroke-width="5"/>
      <rect x="238" y="280" width="166" height="45" fill="var(--sky)"/>
      <text class="stage-name" x="321" y="305" text-anchor="middle">ENTREPRENEUR</text>
      <text class="stage-age" x="321" y="319" text-anchor="middle">0-10 Years</text>
    </g>

    <g class="stage stage-adolescent">
      <circle cx="502" cy="412" r="84" fill="#fff" stroke="var(--green)" stroke-width="5"/>
      <rect x="420" y="380" width="165" height="45" fill="var(--green)"/>
      <text class="stage-name" x="502" y="405" text-anchor="middle">ADOLESCENT</text>
      <text class="stage-age" x="502" y="419" text-anchor="middle">10-15 Years</text>
    </g>

    <g class="stage stage-mature">
      <circle cx="720" cy="388" r="84" fill="#fff" stroke="var(--red)" stroke-width="5"/>
      <rect x="636" y="368" width="167" height="45" fill="var(--red)"/>
      <text class="stage-name" x="720" y="393" text-anchor="middle">MATURE</text>
      <text class="stage-age" x="720" y="407" text-anchor="middle">15-30 Years Plus</text>
    </g>

    <g class="stage stage-dying">
      <circle cx="908" cy="240" r="82" fill="#fff" stroke="var(--violet)" stroke-width="5"/>
      <rect x="832" y="218" width="165" height="45" fill="var(--violet)"/>
      <text class="stage-name" x="915" y="243" text-anchor="middle">DYING</text>
      <text class="stage-age" x="915" y="257" text-anchor="middle">20 Years Plus</text>
    </g>
  </svg>

  <div class="brand-name">HAA</div>

  <p class="copyright">© 2020 All Rights Reserved, Harbor Academy Advisors</p>
</div>
</body>
</html>
```